Property management company looking for modern card design

We at Blue Maple Holdings provides property management services for its residential and commercial properties, with expertise in all categories of multifamily, industrial and office projects throughout California.

We need a business card design that is professional and modern designed business card. In our field, clients get hundreds of business cards, we would like our card to stand out.

Please avoid small print.

Target Market(s)

Professionals and high end clients

Industry/Entity Type

Financial Planning

Contact Information for Business Card

Company Name: Blue Maple Holdings, Name, email, license #, phone number, website bluemapleholdings.example

Font styles to use
Sans Serif

Requirements
Must have
• The card design needs to be adaptable because there is a possibly we will be expanding into different sectors other than real estate. The card design should be focused on financial planning and asset management.
Nice to have
• Modern and simple business card. Eye catching. Non-standard size/shaped cards would be great.
• bluemapleholdings.example
Should not have
• Too many bright color or any pictures or shapes of real estate stuff.

```html
<!DOCTYPE html>
<html lang="en">
<head>
<meta charset="utf-8">
<title>Blue Maple Holdings — Business Card</title>
<link rel="stylesheet" href="https://fonts.googleapis.com/css2?family=Montserrat:wght@600;700&family=Raleway:wght@300;400;600&display=swap">
<style>
  :root {
    --stage: #e9e6e2;
    --red: #c8151f;
    --red-light: #d83a48;
    --black: #151515;
    --card-back: #262626;
    --tile-dark: #343434;
    --white: #ffffff;
    --soft-white: #f3e9ea;
  }
  * { box-sizing: border-box; margin: 0; padding: 0; }
  html, body { width: 1200px; height: 900px; overflow: hidden; }
  body {
    background: var(--stage);
    position: relative;
    font-family: "Raleway", sans-serif;
    color: var(--white);
  }
  .card {
    position: absolute;
    left: 290px;
    width: 620px;
    height: 354px;
    overflow: hidden;
    box-shadow: 0 10px 28px rgba(0,0,0,0.25);
  }

  /* Front */
  .card-front { top: 76px; background: linear-gradient(100deg, var(--red) 30%, var(--red-light)); }
  .front-black-panel {
    position: absolute; left: 0; top: 0; bottom: 0; width: 200px;
    background: var(--black);
  }
  .front-black-panel::after {
    content: ""; position: absolute; left: 200px; top: 0; width: 420px; height: 0;
  }
  .front-lower-band {
    position: absolute; left: 200px; top: 120px; width: 130px; height: 234px;
    background: var(--black);
    clip-path: polygon(0 0, 100% 0, 0 100%);
    display: none;
  }
  .brand-label {
    position: absolute; left: 200px; top: 92px;
    height: 64px; padding: 0 22px 0 16px;
    background: var(--black);
    display: flex; align-items: center; gap: 12px;
  }
  .brand-dot { width: 30px; height: 30px; border-radius: 50%; background: var(--red); flex: none; }
  .brand-name {
    font-family: "Montserrat", sans-serif; font-weight: 600;
    font-size: 21px; letter-spacing: 1px; color: var(--white);
    text-transform: uppercase; white-space: nowrap;
  }

  /* Back */
  .card-back { top: 470px; background: var(--card-back); }
  .tile {
    position: absolute;
    display: flex; flex-direction: column; align-items: center; justify-content: center;
    text-align: center;
  }
  .tile-red { background: linear-gradient(110deg, var(--red), var(--red-light)); }
  .tile-dark { background: var(--tile-dark); }

  .tile-name { left: 10px; top: 10px; width: 236px; height: 178px; align-items: flex-start; padding-left: 28px; }
  .person-name {
    font-family: "Montserrat", sans-serif; font-weight: 700;
    font-size: 27px; color: var(--red); letter-spacing: 0.5px;
  }
  .person-role { font-size: 13px; font-weight: 400; letter-spacing: 0.6px; margin-top: 4px; }

  .tile-license { left: 254px; top: 10px; width: 156px; height: 150px; }
  .license-label { font-family: "Montserrat", sans-serif; font-weight: 700; font-size: 14px; letter-spacing: 0.5px; }
  .license-number { font-size: 15px; font-weight: 300; margin-top: 4px; letter-spacing: 1px; }

  .tile-web { left: 418px; top: 10px; width: 192px; height: 112px; }
  .tile-email { left: 418px; top: 130px; width: 192px; height: 170px; }
  .tile-email, .tile-web { }
  .tile-logo { left: 214px; top: 168px; width: 196px; height: 176px; }
  .tile-phone { left: 10px; top: 196px; width: 196px; height: 148px; }

  .contact-text { font-size: 13px; font-weight: 400; margin-top: 10px; letter-spacing: 0.4px; }
  .phone-text { font-size: 16px; font-weight: 300; letter-spacing: 1px; margin-top: 12px; }
  .icon { width: 34px; height: 34px; }
  .logo-disc { width: 120px; height: 120px; border-radius: 50%; background: var(--red); }
</style>
</head>
<body>

  <section class="card card-front" aria-label="Card front">
    <div class="front-black-panel"></div>
    <div class="brand-label">
      <span class="brand-dot"></span>
      <span class="brand-name">Blue Maple Holdings</span>
    </div>
  </section>

  <section class="card card-back" aria-label="Card back">
    <div class="tile tile-dark tile-name">
      <p class="person-name">YOUR NAME</p>
      <p class="person-role">PROPERTY MANAGEMENT</p>
    </div>

    <div class="tile tile-red tile-license">
      <p class="license-label">LICENSE #</p>
      <p class="license-number">1234567</p>
    </div>

    <div class="tile tile-dark tile-web">
      <svg class="icon" viewBox="0 0 34 34" aria-hidden="true">
        <circle cx="17" cy="17" r="16" fill="#fff"/>
        <g fill="none" stroke="#343434" stroke-width="1.4">
          <circle cx="17" cy="17" r="10"/>
          <ellipse cx="17" cy="17" rx="4.5" ry="10"/>
          <line x1="7" y1="17" x2="27" y2="17"/>
          <line x1="9" y1="12" x2="25" y2="12"/>
          <line x1="9" y1="22" x2="25" y2="22"/>
        </g>
      </svg>
      <p class="contact-text">bluemapleholdings.example</p>
    </div>

    <div class="tile tile-red tile-email">
      <svg class="icon" viewBox="0 0 34 34" aria-hidden="true">
        <circle cx="17" cy="17" r="16" fill="#fff"/>
        <rect x="8" y="11" width="18" height="12" fill="var(--red)"/>
        <polyline points="8,11 17,18 26,11" fill="none" stroke="#fff" stroke-width="1.5"/>
      </svg>
      <p class="contact-text">your email @here.com</p>
    </div>

    <div class="tile tile-dark tile-logo">
      <div class="logo-disc"></div>
    </div>

    <div class="tile tile-red tile-phone">
      <svg class="icon" viewBox="0 0 34 34" aria-hidden="true">
        <circle cx="17" cy="17" r="16" fill="#fff"/>
        <path d="M12 9 l3 0 l1.5 4.5 l-2 1.5 q1.5 3.5 4.5 5 l1.5 -2 l4.5 1.5 l0 3 q-1 1.5 -3 1.5 q-7 -1 -10.5 -9 q-0.5 -4 0.5 -6 z" fill="var(--red)"/>
      </svg>
      <p class="phone-text">12345678910</p>
    </div>
  </section>

</body>
</html>
```